The Juniper Coach

I am a life coach specializing in helping people with depression and bipolar disorder. I would like a nice, fun design for a business card.

```html
<!DOCTYPE html>
<html lang="en">
<head>
<meta charset="utf-8">
<title>The Juniper Coach – Business Card</title>
<link rel="stylesheet" href="https://fonts.googleapis.com/css2?family=Old+Standard+TT:wght@700&display=swap">
<style>
  :root {
    --page-bg: #e9e7e3;
    --card-black: #141316;
    --silver-light: #e4e4e6;
    --silver-mid: #b9b9bc;
    --silver-dark: #4a494c;
    --violet-light: #b7b9de;
    --violet-mid: #7d81b8;
    --violet-deep: #3c4483;
    --ink: #262528;
  }
  * { box-sizing: border-box; margin: 0; padding: 0; }
  html, body {
    width: 1200px;
    height: 1200px;
    overflow: hidden;
    background: var(--page-bg);
  }
  .canvas {
    position: relative;
    width: 1200px;
    height: 1200px;
  }
  .business-card {
    position: absolute;
    left: 100px;
    top: 314px;
    width: 1000px;
    height: 572px;
    overflow: hidden;
    box-shadow: 0 18px 40px rgba(0, 0, 0, 0.18);
  }
  .card-art {
    position: absolute;
    inset: 0;
    width: 100%;
    height: 100%;
    display: block;
  }
  .brand {
    position: absolute;
    left: 70px;
    top: 120px;
    display: flex;
    align-items: flex-start;
    gap: 22px;
  }
  .brand-mark {
    width: 30px;
    height: 30px;
    margin-top: 18px;
    background: var(--ink);
    flex: none;
  }
  .brand-name {
    font-family: "Old Standard TT", "Times New Roman", serif;
    font-weight: 700;
    font-size: 56px;
    line-height: 1.1;
    letter-spacing: 1px;
    text-transform: uppercase;
    color: var(--ink);
    white-space: nowrap;
  }
  .brand-line {
    display: block;
  }
  .brand-rule {
    display: block;
    width: 250px;
    height: 3px;
    margin-top: 8px;
    background: var(--ink);
  }
</style>
</head>
<body>
<main class="canvas">
  <section class="business-card">
    <svg class="card-art" viewBox="0 0 1000 572" preserveAspectRatio="none" aria-hidden="true">
      <defs>
        <linearGradient id="silverSweep" x1="0" y1="1" x2="1" y2="0">
          <stop offset="0" stop-color="var(--silver-dark)"/>
          <stop offset="0.3" stop-color="var(--silver-mid)"/>
          <stop offset="0.75" stop-color="var(--silver-light)"/>
          <stop offset="1" stop-color="#f2f2f3"/>
        </linearGradient>
        <radialGradient id="violetGlow" cx="0.45" cy="0.3" r="0.75">
          <stop offset="0" stop-color="var(--violet-light)"/>
          <stop offset="0.45" stop-color="var(--violet-mid)"/>
          <stop offset="1" stop-color="var(--violet-deep)"/>
        </radialGradient>
      </defs>
      <rect class="card-base" width="1000" height="572" fill="var(--card-black)"/>
      <path class="silver-panel" d="M0,0 H720 C690,280 560,480 300,572 H0 Z" fill="url(#silverSweep)"/>
      <path class="violet-panel" d="M440,572 C620,470 720,320 800,190 C850,120 1000,110 1000,250 V572 Z" fill="url(#violetGlow)"/>
    </svg>
    <div class="brand">
      <span class="brand-mark"></span>
      <div class="brand-text">
        <h1 class="brand-name">
          <span class="brand-line">The Juniper</span>
          <span class="brand-line">Coach</span>
        </h1>
        <span class="brand-rule"></span>
      </div>
    </div>
  </section>
</main>
</body>
</html>
```